文章は添付のテキストのコピペで構いません。
見本の挨拶状はモノクロで、またテキストのみの、
硬い、暗い印象ですので、こちらを女性らしく、
可愛らしく、読みやすくしてください。

お手紙風(便箋風)など良いかもしれません。

初めて商品を手にした方に、買ってよかったと思われる、
ご挨拶状にしたいと思います。
縦書、横書き指定ございません。
記載項目
商品写真、ロゴ、電話番号、営業時間など

```html
<!DOCTYPE html>
<html lang="ja">
<head>
<meta charset="utf-8">
<title>ごあいさつ</title>
<link href="https://fonts.googleapis.com/css2?family=Shippori+Mincho:wght@500;700&family=Zen+Kaku+Gothic+New:wght@400;500&display=swap" rel="stylesheet">
<style>
:root{
  --paper:#ffffff;
  --ink:#4a4446;
  --muted:#6f6668;
  --rose:#e46a8e;
  --rose-soft:#f7c9d6;
  --blush:#fbe4ea;
  --leaf:#d9e6c8;
  --line:#f0b3c4;
}
*{margin:0;padding:0;box-sizing:border-box}
html,body{width:846px;height:1200px;overflow:hidden;background:var(--paper)}
body{position:relative;font-family:"Zen Kaku Gothic New",sans-serif;color:var(--ink);font-size:10.5px;line-height:1.75}
.deco{position:absolute}
.corner-tl{left:0;top:0;width:150px;height:150px;background:radial-gradient(circle at 20% 20%,var(--rose-soft),var(--blush) 45%,transparent 72%)}
.corner-tr{right:0;top:0;width:190px;height:150px;background:radial-gradient(circle at 80% 15%,var(--rose-soft),var(--blush) 45%,transparent 72%)}
.side-l{left:0;top:420px;width:70px;height:220px;background:radial-gradient(ellipse at 0% 50%,var(--blush),transparent 70%)}
.portrait{right:20px;top:40px;width:230px;height:260px;background:radial-gradient(ellipse at 60% 45%,#f6eef0,transparent 70%)}
.bottom-band{left:0;bottom:0;width:846px;height:150px;background:linear-gradient(180deg,transparent 0%,var(--blush) 40%,var(--rose-soft) 75%,var(--leaf) 100%)}
.letter{position:absolute;left:58px;top:26px;width:735px}
h1{font-family:"Shippori Mincho",serif;font-weight:500;text-align:center;font-size:22px;letter-spacing:.25em;color:var(--muted);margin-bottom:8px}
p{margin-bottom:9px}
h2{font-family:"Shippori Mincho",serif;font-weight:700;color:var(--rose);font-size:16px;display:inline-block;border-bottom:1.5px solid var(--line);padding-bottom:2px;margin:4px 0 12px}
.product{position:absolute;left:55px;top:605px;width:105px;height:290px;border-radius:10px 10px 6px 6px;background:linear-gradient(90deg,#2a2022,#5a4448 45%,#2a2022)}
.feature{position:absolute;left:380px;top:625px;width:415px}
.scalp{position:absolute;left:200px;top:730px;width:595px}
.scalp h2{display:block;text-align:center}
.brand{position:absolute;left:80px;top:985px;width:190px;text-align:center;font-family:"Shippori Mincho",serif;color:var(--rose);font-weight:700}
.brand .mark{display:block;width:14px;height:14px;border-radius:50%;background:var(--rose);margin:0 auto 6px}
.brand .name{font-size:30px;letter-spacing:.06em}
.contact{position:absolute;left:420px;top:1000px;font-size:12px;line-height:1.7;color:var(--ink)}
.contact strong{font-weight:500}
.phone{display:inline-block;width:11px;height:11px;vertical-align:-1px;margin-right:3px}
</style>
</head>
<body>
<div class="deco corner-tl" role="img" aria-label="ピンクの花のあしらい"></div>
<div class="deco corner-tr" role="img" aria-label="ピンクの花のあしらい"></div>
<div class="deco side-l" role="img" aria-label="花のあしらい"></div>
<div class="deco portrait" role="img" aria-label="髪の長い女性の淡い線画イラスト"></div>
<div class="deco bottom-band" role="img" aria-label="ピンクの花と葉のボーダー"></div>

<main class="letter">
  <h1>ごあいさつ</h1>
  <p>この度は、数多くのシャンプーの中から、リュミエール「カルムヘアシャンプー」をお選びいただき、誠にありがとうございます。</p>
  <h2>「髪は女の命」</h2>
  <p>艶のある美しい髪は、女性の大きな魅力です。毎日のお手入れが、自信と笑顔を育ててくれます。</p>
  <p>艶がなくパサついている髪は、なんとなく疲れた印象に見えるもの。ボリュームが出ない、まとまらない、カラーの色持ちが悪いなど、髪のお悩みはさまざまです。</p>
  <p>だからこそ、やさしい洗い心地と、しっとりとした仕上がりにこだわりました。毎日使うものだから、安心して使っていただきたい。そんな想いから生まれたシャンプーです。</p>
  <p>頭皮にやさしい洗浄成分を厳選し、うるおいを守りながら汚れをすっきり落とします。髪と頭皮のすこやかさを保つことが、美しい髪への一番の近道と考えています。</p>
  <p>美しい髪を育てるためには、頭皮の環境を整えることが大切です。毎日のシャンプーを見直すことで、髪は少しずつ変わっていきます。</p>
  <p>そこで、私たちは、植物由来の成分を中心に、香りや泡立ちにもこだわり、お使いいただくたびに心がほっとするようなシャンプーを目指しました。</p>
  <p>また、カルムシリーズは、毎日のケアを楽しく続けていただけるよう、トリートメントやヘアオイルもご用意しております。ぜひあわせてお試しください。</p>
</main>

<div class="product" role="img" aria-label="カルムヘアシャンプーのボトル写真"></div>

<section class="feature">
  <p>カルムヘアシャンプーは、うるおいを与えながら汚れをやさしく落とし、髪一本一本をなめらかに整えます。香りは心をほどくフローラル。バスタイムを、自分をいたわる時間に変えてくれます。</p>
  <p>初めての方にも安心してお使いいただけるよう、丁寧にお作りしました。</p>
</section>

<section class="scalp">
  <h2>頭皮のケアは、美しい髪を育てる。</h2>
  <p>お客様の髪が少しでも健やかになりますように。心を込めてお届けいたします。</p>
  <p>また商品についてご不明な点やご質問などございましたら、お気軽にお問い合わせください。</p>
</section>

<div class="brand">
  <span class="mark"></span>
  <span class="name">Lumière</span>
</div>

<div class="contact">
  <strong>リュミエール　お客様サポート</strong><br>
  <svg class="phone" viewBox="0 0 24 24"><path fill="#e46a8e" d="M6.6 10.8a15 15 0 0 0 6.6 6.6l2.2-2.2a1 1 0 0 1 1-.25 11.4 11.4 0 0 0 3.6.57 1 1 0 0 1 1 1V20a1 1 0 0 1-1 1A17 17 0 0 1 3 4a1 1 0 0 1 1-1h3.5a1 1 0 0 1 1 1c0 1.25.2 2.45.57 3.57a1 1 0 0 1-.25 1z"/></svg>フリーダイヤル：0120-000-000<br>
  <span style="font-size:10px">（受付時間 平日 10:00〜17:00）</span><br>
  メール：support@lumiere-example.jp
</div>
</body>
</html>
```